Corbin Haskell International Country Singer

We need a Cd cover for Corbin Haskell. The title is "Ride The Dawn". Really looking for a fresh innovative look at days gone by. Fairly standard brief as far as cd cover's are concerned. looking for a catchy flow through the booklet. Images are available of the artist, more for inside the booklet than for use on the cover.
New CD title: Ride The Dawn
Artist name: Corbin Haskell
Current website: CorbinHaskell.example
Facebook: facebook.com/CorbinHaskell

Industry/Entity Type

Singer

Logo Text

Corbin Haskell Ride The Dawn

Font styles to use
Decorative

```html
<!DOCTYPE html>
<html lang="en">
<head>
<meta charset="utf-8">
<title>Corbin Haskell – Ride The Dawn</title>
<link href="https://fonts.googleapis.com/css2?family=Ultra&family=Pathway+Gothic+One&display=swap" rel="stylesheet">
<style>
  :root {
    --night: #0c0f1c;
    --sky-blue: #2c4a7e;
    --glow: #e9eef8;
    --dusk: #6b5a7a;
    --ember: #d9561e;
    --gold: #c8902f;
    --field: #5a3d1a;
    --shadow: #06060a;
    --title-white: #ffffff;
    --name-grey: #a6a6a6;
  }
  html, body {
    margin: 0;
    padding: 0;
    width: 1200px;
    height: 1079px;
    overflow: hidden;
    background: var(--shadow);
  }
  .cover {
    position: relative;
    width: 1200px;
    height: 1079px;
    overflow: hidden;
  }
  .cover-artwork {
    position: absolute;
    inset: 0;
    width: 1200px;
    height: 1079px;
    display: block;
  }
  .album-title {
    position: absolute;
    left: 107px;
    top: 48px;
    margin: 0;
    font-family: "Pathway Gothic One", "Oswald", sans-serif;
    font-weight: 400;
    font-size: 82px;
    line-height: 1;
    color: var(--title-white);
    letter-spacing: 0.5px;
  }
  .artist-name {
    position: absolute;
    left: 0;
    right: 0;
    top: 930px;
    margin: 0;
    text-align: center;
    font-family: "Ultra", "Rockwell", serif;
    font-weight: 400;
    font-size: 90px;
    line-height: 1;
    color: var(--name-grey);
    letter-spacing: 1px;
  }
</style>
</head>
<body>
  <main class="cover">
    <svg class="cover-artwork" viewBox="0 0 1200 1079" role="img"
         aria-label="Painterly photo of a dark horse with a white blaze walking through golden grass at sunset, a glowing sky behind and a faint close-up eye blended into the upper right">
      <defs>
        <linearGradient id="sceneTones" x1="0" y1="0" x2="0" y2="1">
          <stop offset="0" stop-color="var(--night)"/>
          <stop offset="0.18" stop-color="var(--sky-blue)"/>
          <stop offset="0.36" stop-color="var(--dusk)"/>
          <stop offset="0.45" stop-color="var(--ember)"/>
          <stop offset="0.55" stop-color="var(--gold)"/>
          <stop offset="0.72" stop-color="var(--field)"/>
          <stop offset="0.86" stop-color="var(--shadow)"/>
          <stop offset="1" stop-color="var(--shadow)"/>
        </linearGradient>
        <radialGradient id="sunGlow" cx="0.38" cy="0.3" r="0.28">
          <stop offset="0" stop-color="var(--glow)" stop-opacity="0.85"/>
          <stop offset="1" stop-color="var(--glow)" stop-opacity="0"/>
        </radialGradient>
      </defs>
      <rect width="1200" height="1079" fill="url(#sceneTones)"/>
      <rect width="1200" height="1079" fill="url(#sunGlow)"/>
    </svg>

    <h2 class="album-title">Ride The Dawn</h2>
    <h1 class="artist-name">Corbin Haskell</h1>
  </main>
</body>
</html>
```